Tobin Quartz Portal Page . It's guarantee project!

We need a clean and professional modern web application portal page
That includes the Login & Application Selection screen

Also, I need to design both Desktop and Mobile sizes.
We have an example design for our target

The application is Jetty Schedule and related data.
Our client is a bit conservative.

Theme color preferred : #00508B (main) #DF0D83 (secondary)

Target Market(s)

Oil & Fuel & Gasoline

Number of Pages Required

2 page

Font styles to use
Sans Serif

Colors
0054AA
0677BA
7BADD7
CADEEF
E8F1F8
E54698
E96AAD
F1A4CE
F9D9EA
FCEFF6

Requirements
Must have
• Login Page & Main Screen

```html
<!DOCTYPE html>
<html lang="en">
<head>
<meta charset="UTF-8">
<title>Tobin Quartz Portal – Login</title>
<link rel="stylesheet" href="https://fonts.googleapis.com/css2?family=Poppins:wght@400;500;600&family=Arimo:wght@700&display=swap">
<style>
  :root {
    --brand-blue: #00508B;
    --brand-blue-light: #0677BA;
    --brand-blue-sky: #4AA7DE;
    --brand-pink: #DF0D83;
    --brand-pink-deep: #C2197C;
    --text-muted: #8A8F98;
    --text-dark: #3A3D44;
    --field-border: #B9BEC6;
    --icon-grey: #CFD2D7;
    --page-bg: #FFFFFF;
  }
  * { box-sizing: border-box; margin: 0; padding: 0; }
  html, body { width: 1200px; height: 675px; overflow: hidden; background: var(--page-bg); }
  body { font-family: "Poppins", sans-serif; position: relative; }

  .hero-panel {
    position: absolute; left: 0; top: 0; width: 470px; height: 675px;
    background: var(--brand-blue); overflow: hidden;
  }
  .hero-title {
    position: absolute; top: 88px; left: 0; width: 100%; text-align: center;
    font-family: "Arimo", sans-serif; font-weight: 700; font-size: 35px;
    color: #FFFFFF; letter-spacing: -0.5px;
  }
  .hero-illustration {
    position: absolute; left: 0; right: 0; top: 160px; bottom: 0;
    background: linear-gradient(180deg,
      var(--brand-blue) 0%,
      #3A4D97 14%,
      var(--brand-pink-deep) 30%,
      var(--brand-pink) 45%,
      #9E3C8C 56%,
      #1F5FA6 68%,
      var(--brand-blue-light) 82%,
      var(--brand-blue-sky) 100%);
  }

  .backdrop-curves { position: absolute; left: 470px; top: 0; width: 730px; height: 675px; pointer-events: none; }

  .login-card { position: absolute; left: 576px; top: 0; width: 531px; height: 675px; }
  .login-title {
    position: absolute; top: 90px; left: 0;
    font-size: 25px; font-weight: 600; color: var(--brand-blue); letter-spacing: -0.6px;
  }
  .login-subtitle {
    position: absolute; top: 141px; left: 0; width: 200px;
    font-size: 10.6px; line-height: 13px; color: var(--text-muted);
  }
  .field-label { position: absolute; left: 0; font-size: 10.6px; color: var(--text-muted); }
  .field {
    position: absolute; left: -1px; width: 532px; height: 48px;
    border: 1px solid var(--field-border); border-radius: 3px; background: #FFFFFF;
    display: flex; align-items: center; padding: 0 20px;
    font-size: 11px; color: var(--text-dark);
  }
  .field-value { flex: 1; }
  .field-icon { color: var(--icon-grey); font-size: 15px; margin-right: 34px; display: flex; }
  .label-user { top: 216px; }
  .field-user { top: 243px; }
  .label-pass { top: 316px; }
  .field-pass { top: 344px; letter-spacing: 0.5px; }

  .form-options {
    position: absolute; top: 429px; left: 0; width: 510px;
    display: flex; justify-content: space-between; align-items: center; font-size: 10.5px;
  }
  .remember { display: flex; align-items: center; gap: 6px; color: var(--text-dark); }
  .forgot-link { color: var(--text-muted); text-decoration: none; }

  .login-button {
    position: absolute; top: 479px; left: -1px; width: 532px; height: 48px;
    border: none; border-radius: 3px; background: var(--brand-pink); color: #FFFFFF;
    font-family: "Arimo", sans-serif; font-size: 15px; font-weight: 700; letter-spacing: -0.3px;
    box-shadow: 0 8px 18px rgba(223,13,131,0.12);
  }
  .signup-line { position: absolute; top: 566px; left: 0; font-size: 11px; color: var(--text-muted); }
  .signup-line a { color: var(--brand-pink); text-decoration: none; font-weight: 500; margin-left: 4px; }
</style>
</head>
<body>
  <section class="hero-panel">
    <h1 class="hero-title">Welcome Back!</h1>
    <div class="hero-illustration" role="img" aria-label="Illustration of an offshore oil rig with a supply ship on blue waves"></div>
  </section>

  <svg class="backdrop-curves" viewBox="0 0 730 675" aria-hidden="true">
    <defs>
      <linearGradient id="curve-fade" x1="0" y1="0" x2="0" y2="1">
        <stop offset="0" stop-color="#EDF1F5" stop-opacity="0.9"/>
        <stop offset="0.7" stop-color="#F1F4F7" stop-opacity="0.6"/>
        <stop offset="1" stop-color="#FFFFFF" stop-opacity="0"/>
      </linearGradient>
    </defs>
    <path d="M360 0 C 470 40, 535 110, 540 210 C 545 150, 560 60, 552 0 Z" fill="url(#curve-fade)"/>
    <path d="M552 0 C 565 60, 560 150, 540 210 C 600 140, 630 70, 610 0 Z" fill="url(#curve-fade)" opacity="0.7"/>
    <path d="M640 0 C 690 70, 700 140, 690 205 C 720 160, 730 110, 730 60 L 730 0 Z" fill="url(#curve-fade)"/>
  </svg>

  <main class="login-card">
    <h2 class="login-title">Login</h2>
    <p class="login-subtitle">Welcome back! Please login to your account.</p>

    <label class="field-label label-user">User Name</label>
    <div class="field field-user">
      <span class="field-value">Test@tobinmail.com</span>
      <span class="field-icon">@</span>
    </div>

    <label class="field-label label-pass">Password</label>
    <div class="field field-pass">
      <span class="field-value">***********</span>
      <span class="field-icon">
        <svg width="13" height="16" viewBox="0 0 13 16"><path d="M3 7V4.5a3.5 3.5 0 0 1 7 0V7" fill="none" stroke="#CFD2D7" stroke-width="1.8"/><rect x="0" y="7" width="13" height="9" rx="1.5" fill="#CFD2D7"/></svg>
      </span>
    </div>

    <div class="form-options">
      <span class="remember">
        <svg width="13" height="13" viewBox="0 0 13 13"><circle cx="6.5" cy="6.5" r="6.5" fill="#DF0D83"/><path d="M3.6 6.7l2 2 3.8-4" fill="none" stroke="#FFFFFF" stroke-width="1.5" stroke-linecap="round" stroke-linejoin="round"/></svg>
        Remember Me
      </span>
      <a class="forgot-link" href="#">Forget Password?</a>
    </div>

    <button class="login-button" type="button">Login</button>

    <p class="signup-line">New User ? <a href="#">Signup</a></p>
  </main>
</body>
</html>
```